Marketing One-Sheet for Security Deposit Claim Notice

I need a one-sheet flyer formatted for email distribution — optimized as a JPEG/PNG that I can insert into Constant Contact or Outlook. I do not want to attach it to an email, but insert it in the email we send out. I would like it to look professional but engaging. Some images would be good, but want to make sure it reads well if images do not load for the recipients. The text is in the attached Word document, but I am open to changes/ideas that may be better for marketing purposes. I included the URLs for some of the links I would like in the one-sheet that is clickable. The logo for the business is being uploaded on the Word document. Proposed text is also uploaded in a Word document. Thank you.

Target Market(s)

Landlords, Real Estate Agents, Property Managers

Industry/Entity Type

Legal

Requirements
Must have
• Professional but appealing design. The One-sheet is going to be placed in the body of emails, not as an attachment.
Nice to have
• Include our logo for the business and the web links please.
Should not have
• Images can be ok, but it needs to look right if images do not download from the email sent out.

```html
<!DOCTYPE html>
<html lang="en">
<head>
<meta charset="utf-8">
<title>Security Deposit Claim Notice</title>
<link rel="stylesheet" href="https://fonts.googleapis.com/css2?family=Roboto:wght@400;500;700;900&family=Roboto+Condensed:wght@400;700&display=swap">
<style>
  :root {
    --page: #ffffff;
    --ink: #050608;
    --white: #ffffff;
    --accent: #138ac2;
    --hero-deep: #04101f;
    --hero-mid: #0d3a63;
    --hero-glow: #2a86c4;
  }
  * { margin: 0; padding: 0; box-sizing: border-box; }
  html, body { width: 1007px; height: 1200px; overflow: hidden; background: var(--page); }
  body { font-family: "Roboto", Arial, sans-serif; color: var(--white); }

  .flyer {
    position: absolute; left: 54px; top: 20px;
    width: 898px; height: 1160px;
    background: var(--ink); overflow: hidden;
  }
  .hero {
    position: absolute; left: 0; top: 0; width: 898px; height: 760px;
    background:
      radial-gradient(ellipse 40% 45% at 38% 46%, #2b2f36 0%, #14171c 55%, transparent 75%),
      radial-gradient(ellipse 60% 40% at 80% 70%, var(--hero-glow) 0%, transparent 70%),
      linear-gradient(180deg, var(--hero-mid) 0%, var(--hero-deep) 70%, var(--ink) 100%);
  }
  .hero-title {
    position: absolute; right: 51px; top: 58px;
    text-align: right; font-weight: 700; font-size: 70px; line-height: 63px;
    letter-spacing: -0.5px;
  }
  .hero-subtitle {
    position: absolute; right: 51px; top: 256px;
    text-align: right; font-weight: 500; font-size: 30px; line-height: 28px;
  }
  .benefit {
    position: absolute; width: 166px; height: 166px; border-radius: 50%;
    background: var(--accent);
    display: flex; align-items: center; justify-content: center;
    text-align: center; font-weight: 700;
  }
  .benefit--rent { left: 550px; top: 336px; font-size: 33px; line-height: 33px; }
  .benefit--fees { left: 676px; top: 465px; font-size: 27px; line-height: 27px; }
  .benefit--damage { left: 504px; top: 523px; font-size: 23px; line-height: 23px; }

  .service-title {
    position: absolute; left: 43px; top: 740px;
    font-weight: 700; font-size: 48px; line-height: 45px; letter-spacing: -0.3px;
  }
  .price-tag {
    position: absolute; left: 254px; top: 918px; width: 102px; height: 46px;
    background: var(--accent); text-align: center; font-weight: 700;
  }
  .price-tag .amount { display: block; font-size: 29px; line-height: 30px; margin-top: 1px; }
  .price-tag .note { display: block; font-size: 13px; line-height: 13px; letter-spacing: 0.5px; }

  .follow-icon { position: absolute; left: 46px; top: 978px; }
  .law-note {
    position: absolute; left: 110px; top: 993px;
    font-size: 12.5px; line-height: 16px; font-weight: 400;
  }
  .more-label {
    position: absolute; left: 47px; top: 1051px; padding: 2px 9px;
    background: var(--accent); font-size: 10px; font-weight: 700; line-height: 15px;
  }
  .more-link {
    position: absolute; left: 47px; top: 1078px;
    font-size: 11.5px; color: var(--white); text-decoration: none;
  }

  .divider {
    position: absolute; left: 373px; top: 785px; width: 2px; height: 250px;
    background: var(--white);
  }

  .risk-heading {
    position: absolute; left: 391px; top: 744px; width: 430px;
    font-family: "Roboto Condensed", "Arial Narrow", sans-serif;
    font-weight: 700; font-size: 21px; line-height: 27px;
  }
  .risk-list {
    position: absolute; left: 391px; top: 804px; list-style: none;
    font-size: 13.2px; line-height: 16.5px;
  }
  .risk-list li::before { content: "- "; }
  .risk-detail {
    position: absolute; left: 391px; top: 858px; width: 448px;
    font-family: "Roboto Condensed", "Arial Narrow", sans-serif;
    font-weight: 700; font-size: 15.5px; line-height: 18.5px;
  }
  .commercial-fee {
    position: absolute; left: 391px; top: 958px; width: 389px; height: 23px;
    background: var(--accent);
    font-family: "Roboto Condensed", "Arial Narrow", sans-serif;
    font-weight: 700; font-size: 15px; line-height: 23px;
    padding-left: 12px;
  }

  .doc-icon { position: absolute; left: 391px; top: 1002px; }
  .hire-label {
    position: absolute; left: 449px; top: 1003px;
    font-weight: 700; font-size: 12.8px; line-height: 16px;
  }
  .hire-link {
    position: absolute; left: 400px; top: 1070px; width: 232px; height: 19px;
    background: var(--accent); color: var(--white); text-decoration: none;
    font-size: 11.5px; line-height: 19px; padding-left: 9px;
  }

  .brand { position: absolute; left: 645px; top: 995px; width: 230px; }
  .brand-mark { display: flex; align-items: flex-start; gap: 8px; }
  .brand-name {
    font-weight: 400; font-size: 27px; line-height: 28px; color: var(--white);
  }
  .brand-square { width: 38px; height: 38px; background: var(--white); margin-top: 24px; }
  .brand-tagline {
    margin-top: 6px; font-size: 9.5px; line-height: 11px; padding-left: 4px;
  }
  .brand-contact {
    margin-top: 6px; width: 200px; text-align: center;
    font-weight: 700; font-size: 15.5px; line-height: 20px;
  }
</style>
</head>
<body>
<main class="flyer">
  <section class="hero" role="img" aria-label="Open steel bank vault door glowing with blue digital code streams"></section>

  <h1 class="hero-title">SECURITY<br>DEPOSIT<br>CLAIM NOTICE</h1>
  <p class="hero-subtitle">KEEP THE TENANT'S<br>SECURITY DEPOSITE</p>

  <div class="benefit benefit--rent">COVER<br>UNPAID<br>RENT</div>
  <div class="benefit benefit--fees">APPLY TO<br>LEGAL<br>FEES AND<br>COSTS</div>
  <div class="benefit benefit--damage">CHARGE<br>AGAINST<br>DAMAGES<br>TO THE<br>PROPERTY</div>

  <h2 class="service-title">WE PREPARE<br>SECURITY<br>DEPOSIT<br>CLAIM<br>NOTICES</h2>
  <div class="price-tag"><span class="amount">$350</span><span class="note">FLAT FEE</span></div>

  <svg class="follow-icon" width="56" height="56" viewBox="0 0 56 56" aria-hidden="true">
    <rect x="1" y="1" width="54" height="18" rx="4" fill="none" stroke="#fff" stroke-width="1.5"/>
    <text x="28" y="14.5" text-anchor="middle" font-family="Roboto, Arial, sans-serif" font-size="12" fill="#fff">follow</text>
    <path d="M24 22 v18 M24 30 h10 a3 3 0 0 1 3 3 v10 a8 8 0 0 1 -8 8 h-4 a8 8 0 0 1 -7 -4 l-4 -8" fill="none" stroke="#fff" stroke-width="1.5" stroke-linecap="round"/>
  </svg>
  <p class="law-note">FLORIDA LAW TO KEEP<br>THE DEPOSIT</p>
  <span class="more-label">MORE INFORMATION</span>
  <a class="more-link" href="https://tenancylegalgroup.com/keeping-security-deposits/1">https://tenancylegalgroup.com/keeping-security-deposits/1</a>

  <div class="divider"></div>

  <h3 class="risk-heading">If the Security Deposit Claim is not made correctly and on time, then:</h3>
  <ul class="risk-list">
    <li>Tenant is automatically entitled to their full deposit back</li>
    <li>No claim against the deposit can be made</li>
    <li>Tenant can sue and recover the deposit and thousands in legal fees</li>
  </ul>
  <p class="risk-detail">There are lawyers that specialize in representing tenants and go after landlords that do not make a proper claim against the security deposit. They sue and win their cases and get thousands of dollars in legal fees against Landlords, even if the tenant owes unpaid rent.</p>
  <p class="commercial-fee">For commercial properties, the flat legal fee is $450</p>

  <svg class="doc-icon" width="52" height="60" viewBox="0 0 52 60" aria-hidden="true">
    <path d="M8 6 h28 l10 10 v40 h-38 z" fill="none" stroke="var(--accent)" stroke-width="3" stroke-linejoin="round"/>
    <circle cx="10" cy="12" r="9" fill="var(--ink)" stroke="var(--accent)" stroke-width="3"/>
    <path d="M6 12 l3 3 l6 -6" fill="none" stroke="var(--accent)" stroke-width="2.5" stroke-linecap="round"/>
    <path d="M22 22 h16 M16 30 h22 M16 37 h22" stroke="var(--accent)" stroke-width="3" stroke-linecap="round"/>
    <path d="M14 48 l5 -5 l4 4 l6 -6" fill="none" stroke="var(--accent)" stroke-width="2.5" stroke-linecap="round"/>
  </svg>
  <p class="hire-label">REQUEST<br>OUR HIRING<br>DOCUMENTS</p>
  <a class="hire-link" href="https://tenancylegalgroup.com/hire-lawyer/">https://tenancylegalgroup.com/hire-lawyer/</a>

  <div class="brand">
    <div class="brand-mark">
      <span class="brand-name">TENANCY<br>LEGAL GROUP</span>
      <span class="brand-square"></span>
    </div>
    <p class="brand-tagline">a Legal Resource for Landlords,<br>Investors &amp; Property Managers</p>
    <p class="brand-contact">TenancyLegalGroup.com<br>1(800) 555-0142</p>
  </div>
</main>
</body>
</html>
```